Social Media Graphics - Copperfield Loop

Create 6-7 individual social media graphics (square size) to encourage folks to join our online course, using either of the text below (only one set of text per graphic:

The Lantern Ridge Method
How to Create a 7-Figure Business From Scratch
Sign Up Today!

Or

The Lantern Ridge Method
Fast-track Your Way to a Multi-Million Business!
Sign Up Today!

For the color scheme of the graphics, use 1 or 2 colors in the color palette attached; or use any colors that look nice with their outfits; AVOID using red, white and blue altogether because it will look like an Independence Day (4th of July) graphic and we don’t want that; make sure the graphics appeal to both men and women

Make sure each graphic contains 1 of the 2 pics attached; and make sure one of the graphics is all TEXT only.

Target Market(s)

men and women looking to make more money

Industry/Entity Type

entrepreneurship

Requirements
Must have
• see the text document attached
Nice to have
• We are open to a nice color design; the color palette colors are not required, especially we don't want red, white and blue used together
Should not have
• AVOID using red, white and blue altogether because it will look like an Independence Day (4th of July) graphic and we dont want that

```html
<!DOCTYPE html>
<html lang="en">
<head>
<meta charset="utf-8">
<title>The Lantern Ridge Method – Social Tiles</title>
<link rel="stylesheet" href="https://fonts.googleapis.com/css2?family=Anton&family=Oswald:wght@500;600;700&family=Montserrat:ital,wght@0,800;0,900;1,500&family=Lobster&family=Kalam:wght@700&display=swap">
<style>
  :root{
    --page:#160d2e;
    --plum:#3a1079;
    --plum-deep:#2a0a5c;
    --berry:#c8177a;
    --pink:#f8b4d2;
    --orchid:#7a1a78;
    --white:#ffffff;
  }
  *{margin:0;padding:0;box-sizing:border-box}
  html,body{width:1200px;height:792px;overflow:hidden;background:var(--page)}
  .board{position:relative;width:1200px;height:792px}
  .tile{position:absolute;width:349px;height:349px;overflow:hidden}
  .t1{left:54px;top:36px;background:var(--pink)}
  .t2{left:426px;top:36px;background:linear-gradient(160deg,var(--berry) 0%,var(--orchid) 40%,var(--plum) 80%)}
  .t3{left:798px;top:36px;background:var(--plum)}
  .t4{left:54px;top:408px;background:var(--plum)}
  .t5{left:426px;top:408px;background:var(--berry)}
  .t6{left:798px;top:408px;background:var(--berry)}
  .abs{position:absolute}
  .shape{position:absolute;left:0;top:0;width:349px;height:349px}
  .photo{position:absolute}
  .cta{position:absolute;font-family:Oswald,sans-serif;font-weight:600;line-height:1;padding:4px 5px;border-radius:3px;white-space:nowrap}
  .cursor{position:absolute;width:16px;height:18px}

  /* tile 1 */
  .t1 .brand{left:0;width:349px;top:18px;text-align:center;font-family:Kalam,cursive;color:var(--white);font-size:21px}
  .t1 .head{left:30px;top:74px;width:290px;text-align:center;line-height:.95;text-transform:uppercase}
  .t1 .l1{font-family:Anton,sans-serif;color:var(--plum);font-size:58px;letter-spacing:-.5px}
  .t1 .l2{font-family:Oswald,sans-serif;font-weight:500;color:var(--berry);font-size:34px}
  .t1 .l3{font-family:Anton,sans-serif;color:var(--plum);font-size:50px}
  .t1 .l4{font-family:Anton,sans-serif;color:var(--berry);font-size:62px}
  .t1 .cta{left:116px;top:286px;background:var(--white);color:var(--plum);font-size:20px}

  /* tile 2 */
  .t2 .photo{left:0;top:92px;width:235px;height:257px;background:linear-gradient(180deg,#5a2a4a,#1b1428)}
  .t2 .brand{right:24px;top:22px;text-align:right;line-height:.9;font-family:Montserrat,sans-serif;font-weight:900}
  .t2 .b-the{color:var(--pink);font-size:18px}
  .t2 .b-big{color:var(--pink);font-size:38px;letter-spacing:-1px}
  .t2 .b-mid{color:var(--white);font-size:44px;letter-spacing:-1px}
  .t2 .b-sub{color:var(--pink);font-size:15px;letter-spacing:1px}
  .t2 .tag{right:24px;top:232px;text-align:right;font-family:Montserrat,sans-serif;font-weight:900;color:var(--white);font-size:15px;line-height:1.1}
  .t2 .cta{right:25px;top:293px;background:var(--pink);color:var(--berry);font-size:16px}

  /* tile 3 */
  .t3 .card{left:38px;top:30px;width:269px;height:260px;background:var(--white);border-radius:10px}
  .t3 .brand{left:38px;top:44px;width:269px;text-align:center;line-height:.92}
  .t3 .b-the{font-family:Lobster,cursive;color:var(--berry);font-size:38px}
  .t3 .b-red{font-family:Montserrat,sans-serif;font-weight:900;color:var(--berry);font-size:50px;letter-spacing:-2px}
  .t3 .b-navy{font-family:Montserrat,sans-serif;font-weight:900;color:var(--plum);font-size:62px;letter-spacing:-3px}
  .t3 .b-script{font-family:Lobster,cursive;color:var(--berry);font-size:44px}
  .t3 .tag{left:40px;top:300px;font-family:Montserrat,sans-serif;font-style:italic;font-weight:500;color:var(--white);font-size:11.5px;line-height:1.35}
  .t3 .cta{left:215px;top:301px;background:var(--pink);color:var(--berry);font-size:15px}

  /* tile 4 */
  .t4 .the{left:26px;top:62px;transform:rotate(-90deg);transform-origin:left top;font-family:Montserrat,sans-serif;font-weight:900;color:var(--white);font-size:18px}
  .t4 .title{left:50px;top:22px;font-family:Montserrat,sans-serif;font-weight:900;color:var(--white);font-size:40px;letter-spacing:-1px;line-height:1}
  .t4 .sub{right:38px;top:82px;font-family:Montserrat,sans-serif;font-weight:900;color:var(--pink);font-size:20px;letter-spacing:.5px}
  .t4 .photo{left:40px;top:110px;width:290px;height:239px;background:linear-gradient(180deg,#3a2f4a,#2a1a5a)}
  .t4 .tag{left:26px;top:240px;font-family:Oswald,sans-serif;font-weight:500;color:var(--white);font-size:26px;line-height:1.2;text-transform:uppercase}
  .t4 .tag .hl{background:var(--white);color:var(--berry);padding:0 4px}
  .t4 .cta{left:238px;top:296px;background:var(--berry);color:var(--white);font-size:13px}

  /* tile 5 */
  .t5 .photo{left:10px;top:0;width:339px;height:200px;background:linear-gradient(180deg,#e0408a,#a0125e)}
  .t5 .brand{left:18px;top:194px;width:135px;text-align:center;font-family:Montserrat,sans-serif;font-weight:900;line-height:.9}
  .t5 .b-the{color:var(--pink);font-size:11px;margin-bottom:6px}
  .t5 .b-w{color:var(--white);font-size:28px;letter-spacing:-1px}
  .t5 .b-p{color:var(--pink);font-size:30px;letter-spacing:-1px}
  .t5 .b-s{color:var(--white);font-size:13px;margin-top:4px}
  .t5 .rule{left:169px;top:200px;width:1px;height:130px;background:rgba(255,255,255,.5)}
  .t5 .tag{left:192px;top:208px;font-family:Oswald,sans-serif;font-weight:700;color:var(--white);font-size:21px;line-height:1.02}
  .t5 .cta{left:194px;top:306px;background:var(--berry);color:var(--white);font-size:14px}

  /* tile 6 */
  .t6 .photo{left:140px;top:110px;width:209px;height:239px;background:linear-gradient(180deg,#d8508e,#2a1a30)}
  .t6 .title{left:22px;top:110px;transform:rotate(-15deg);transform-origin:left top;font-family:Montserrat,sans-serif;font-weight:900;color:var(--white);font-size:23px;line-height:1.05;letter-spacing:-.5px;white-space:nowrap}
  .t6 .tag{left:28px;top:190px;font-family:Oswald,sans-serif;font-weight:500;color:var(--white);font-size:25px;line-height:1.08;text-transform:uppercase}
  .t6 .cta{left:28px;top:308px;background:var(--pink);color:var(--berry);font-size:14px}
</style>
</head>
<body>
<svg width="0" height="0" style="position:absolute" aria-hidden="true">
  <symbol id="pointer" viewBox="0 0 16 18"><path d="M2 1 L2 15 L6 11.5 L9 17 L11.5 15.8 L8.6 10.4 L13.5 10 Z" fill="#fff" stroke="#160d2e" stroke-width="1"/></symbol>
</svg>
<main class="board">

  <!-- Fast-track, text only -->
  <section class="tile t1">
    <svg class="shape" viewBox="0 0 349 349" aria-hidden="true">
      <path d="M0 0 H349 V58 Q174 78 0 40 Z" fill="var(--berry)"/>
      <path d="M0 330 Q174 270 349 322 V349 H0 Z" fill="var(--plum)"/>
    </svg>
    <div class="abs brand">The Lantern Ridge Method</div>
    <div class="abs head">
      <div class="l1">Fast-Track</div>
      <div class="l2">Your Way to a</div>
      <div class="l3">Multi-Million</div>
      <div class="l4">Business!</div>
    </div>
    <div class="cta">SIGN UP TODAY!</div>
    <svg class="cursor" style="left:218px;top:308px"><use href="#pointer"/></svg>
  </section>

  <!-- 7-figure, duo photo on gradient -->
  <section class="tile t2">
    <div class="photo" role="img" aria-label="Photo of the two course hosts standing together, arms crossed"></div>
    <div class="abs brand">
      <div class="b-the">the</div>
      <div class="b-big">LANTERN</div>
      <div class="b-mid">RIDGE</div>
      <div class="b-sub">METHOD</div>
    </div>
    <div class="abs tag">How to Create a<br>7-Figure Business<br>From Scratch</div>
    <div class="cta">SIGN UP TODAY!</div>
    <svg class="cursor" style="left:310px;top:316px"><use href="#pointer"/></svg>
  </section>

  <!-- 7-figure, title card -->
  <section class="tile t3">
    <div class="abs card"></div>
    <div class="abs brand">
      <div class="b-the">The</div>
      <div class="b-red">Lantern</div>
      <div class="b-navy">Ridge</div>
      <div class="b-script">Method</div>
    </div>
    <div class="abs tag">How to Create a 7-Figure<br>Business From Scratch</div>
    <div class="cta">SIGN UP TODAY!</div>
    <svg class="cursor" style="left:295px;top:324px"><use href="#pointer"/></svg>
  </section>

  <!-- 7-figure, rings -->
  <section class="tile t4">
    <svg class="shape" viewBox="0 0 349 349" aria-hidden="true">
      <circle cx="70" cy="150" r="40" fill="none" stroke="var(--berry)" stroke-width="22"/>
      <circle cx="290" cy="210" r="46" fill="none" stroke="var(--berry)" stroke-width="22"/>
    </svg>
    <div class="photo" role="img" aria-label="Photo of the two course hosts, one in a black turtleneck, one in a denim jacket"></div>
    <div class="abs the">THE</div>
    <div class="abs title">LANTERN RIDGE</div>
    <div class="abs sub">METHOD</div>
    <div class="abs tag">How to create a<br><span class="hl">7-Figure Business</span><br>From Scratch</div>
    <div class="cta">SIGN UP TODAY!</div>
    <svg class="cursor" style="left:302px;top:315px"><use href="#pointer"/></svg>
  </section>

  <!-- 7-figure, wave split -->
  <section class="tile t5">
    <div class="photo" role="img" aria-label="Photo of the two smiling course hosts on a berry backdrop"></div>
    <svg class="shape" viewBox="0 0 349 349" aria-hidden="true">
      <path d="M0 200 Q150 150 260 205 Q320 220 349 160 V349 H0 Z" fill="var(--pink)"/>
      <path d="M0 210 Q150 165 260 212 Q320 230 349 175 V349 H0 Z" fill="var(--plum)"/>
    </svg>
    <div class="abs brand">
      <div class="b-the">THE</div>
      <div class="b-w">LANTERN</div>
      <div class="b-p">RIDGE</div>
      <div class="b-s">METHOD</div>
    </div>
    <div class="abs rule"></div>
    <div class="abs tag">How to Create<br>a 7-Figure<br>Business From<br>Scratch</div>
    <div class="cta">SIGN UP TODAY!</div>
    <svg class="cursor" style="left:280px;top:318px"><use href="#pointer"/></svg>
  </section>

  <!-- Fast-track, diagonal band -->
  <section class="tile t6">
    <svg class="shape" viewBox="0 0 349 349" aria-hidden="true">
      <path d="M60 20 L200 0 L215 0 L62 50 Z" fill="var(--pink)"/>
      <path d="M0 85 L349 -10 V60 L0 170 Z" fill="var(--plum)"/>
      <path d="M0 170 L349 60 V70 L0 182 Z" fill="var(--pink)"/>
    </svg>
    <div class="photo" role="img" aria-label="Photo of the two course hosts, one in a pink dress, one in black"></div>
    <div class="abs title">THE LANTERN RIDGE<br>METHOD</div>
    <svg class="cursor" style="left:312px;top:44px;width:20px;height:23px"><use href="#pointer"/></svg>
    <div class="abs tag">Fast Track<br>Your Way to a<br>Multi-Million<br>Business!</div>
    <div class="cta">SIGN UP TODAY!</div>
  </section>

</main>
</body>
</html>
```